Criação de Layout Web-Design para Verdejar & Campos
A empresa queria:
" Empresa de alto conhecimento técnico em controle de pragas que realizará desinsetização,desratização,repelência de animais peçonhentos e morcegos,e controle de todos os tipo de pragas consideradas urbanas e de grãos armazenados. Sempre buscando soluções inovadoras,novas tecnologias,levando sempre as medidas de segurança e sustentabilidade em primeiro lugar. Lembrando que o foco principal da empresa é o controle de pragas de grãos armazenados. "

```html
<!DOCTYPE html>
<html lang="pt-BR">
<head>
<meta charset="utf-8">
<title>Verdejar &amp; Campos — Novidades Detalhes</title>
<link href="https://fonts.googleapis.com/css2?family=Open+Sans:wght@400;600;700&family=Roboto+Condensed:wght@700&display=swap" rel="stylesheet">
<style>
  :root{
    --top-blue:#3b9be0;
    --brand-blue:#1d5ea9;
    --btn-blue:#1f5aa6;
    --nav-green:#2f9e43;
    --nav-green-dark:#26863a;
    --nav-active:#5dbb62;
    --page-gray:#eef0f2;
    --panel:#ffffff;
    --line:#d7dbe0;
    --text:#4a4f55;
    --muted:#8a9097;
    --photo-a:#c9ccd0;
    --photo-b:#3e5f8f;
    --thumb-a:#7fa3c9;
    --thumb-b:#c9874a;
  }
  *{box-sizing:border-box;margin:0;padding:0}
  html,body{width:1200px;height:1200px;overflow:hidden}
  body{background:var(--page-gray);font-family:"Open Sans",Arial,sans-serif;color:var(--text)}
  .top-strip{height:16px;background:var(--top-blue)}
  .site-header{height:150px;background:var(--panel);display:flex;align-items:center;padding:0 70px;gap:40px}
  .brand{display:flex;align-items:center;gap:14px;width:330px}
  .brand-dot{width:52px;height:52px;border-radius:50%;background:var(--nav-green)}
  .brand-name{font-family:"Open Sans",Arial,sans-serif;font-weight:700;font-size:30px;color:var(--brand-blue)}
  .header-contact{flex:1;display:flex;flex-direction:column;align-items:center;gap:8px}
  .contact-label{font-size:13px;font-weight:700;color:var(--muted);text-transform:uppercase;letter-spacing:.5px}
  .contact-phone{font-size:24px;font-weight:700;color:var(--brand-blue)}
  .header-buttons{display:flex;gap:10px}
  .btn{background:var(--btn-blue);color:#fff;font-size:12px;font-weight:700;text-transform:uppercase;padding:8px 16px;border-radius:3px}
  .client-area{width:300px;display:flex;flex-direction:column;gap:8px}
  .client-title{font-size:12px;font-weight:700;color:var(--muted);text-transform:uppercase}
  .client-row{display:flex;gap:8px}
  .field{flex:1;height:32px;border:1px solid var(--line);border-radius:3px;font-size:12px;color:var(--muted);padding:7px 10px;background:#fafbfc}
  .btn-enter{background:var(--btn-blue);color:#fff;font-size:12px;font-weight:700;text-transform:uppercase;width:70px;border-radius:3px;display:flex;align-items:center;justify-content:center}
  .main-nav{height:54px;background:var(--nav-green);border-bottom:4px solid var(--nav-green-dark);display:flex;padding:0 70px}
  .nav-item{color:#fff;font-family:"Roboto Condensed",Arial,sans-serif;font-weight:700;font-size:15px;text-transform:uppercase;padding:0 26px;display:flex;align-items:center}
  .nav-item.is-active{background:var(--nav-active)}
  .content{display:flex;gap:30px;padding:34px 70px 0}
  .article{flex:1;background:var(--panel);border:1px solid var(--line);height:946px;padding:28px 34px;overflow:hidden}
  .page-title{font-size:24px;font-weight:600;color:#555b62;letter-spacing:.5px}
  .breadcrumb{font-size:12px;color:var(--muted);margin:4px 0 22px;padding-bottom:16px;border-bottom:1px solid var(--line)}
  .category{font-size:13px;font-weight:700;color:var(--nav-green)}
  .headline{font-size:30px;line-height:1.22;font-weight:700;color:var(--brand-blue);margin:6px 0 8px}
  .date{font-size:12px;color:var(--muted);margin-bottom:18px}
  .article-photo{width:100%;height:600px;background:linear-gradient(135deg,var(--photo-b) 0%,#5c7aa6 35%,var(--photo-a) 60%,#e3e5e8 100%)}
  .sidebar{width:300px;background:var(--panel);border:1px solid var(--line);height:946px;padding:28px 22px}
  .side-title{font-size:14px;font-weight:700;color:#555b62;text-transform:uppercase;margin-bottom:10px}
  .side-search{height:32px;border:1px solid var(--line);border-radius:3px;font-size:12px;color:var(--muted);padding:7px 10px;margin-bottom:22px}
  .news-list{list-style:none;display:flex;flex-direction:column;gap:16px}
  .news-item{display:flex;gap:12px;align-items:center;padding-bottom:16px;border-bottom:1px solid var(--line)}
  .news-thumb{width:64px;height:48px;flex:none;background:linear-gradient(135deg,var(--thumb-a),var(--thumb-b))}
  .news-text{font-size:13px;line-height:1.35;font-weight:600;color:var(--brand-blue)}
</style>
</head>
<body>
  <div class="top-strip"></div>
  <header class="site-header">
    <div class="brand">
      <span class="brand-dot"></span>
      <span class="brand-name">Verdejar &amp; Campos</span>
    </div>
    <div class="header-contact">
      <span class="contact-label">Fale com um especialista</span>
      <span class="contact-phone">(51) 3000-4521</span>
      <div class="header-buttons">
        <span class="btn">Fale conosco</span>
        <span class="btn">Solicite orçamento</span>
      </div>
    </div>
    <div class="client-area">
      <span class="client-title">Área do cliente</span>
      <div class="client-row"><span class="field">Usuário</span></div>
      <div class="client-row"><span class="field">Senha</span><span class="btn-enter">Entrar</span></div>
    </div>
  </header>
  <nav class="main-nav">
    <span class="nav-item">Home</span>
    <span class="nav-item">Empresa</span>
    <span class="nav-item">Serviços</span>
    <span class="nav-item is-active">Notícias</span>
    <span class="nav-item">Vídeos</span>
    <span class="nav-item">Contato</span>
  </nav>
  <main class="content">
    <article class="article">
      <h1 class="page-title">Novidades Detalhes</h1>
      <p class="breadcrumb">Você está em: Notícias / Detalhes</p>
      <span class="category">Notícias</span>
      <h2 class="headline">Vazamento de gás de amônia mobiliza equipes de emergência no Polo Industrial de Cubatão, SP</h2>
      <p class="date">Publicado em 14/03/2024</p>
      <div class="article-photo" role="img" aria-label="Foto de técnico com capacete azul e luvas amarelas inspecionando equipamento industrial"></div>
    </article>
    <aside class="sidebar">
      <h3 class="side-title">Buscar notícias</h3>
      <div class="side-search">Digite aqui</div>
      <ul class="news-list">
        <li class="news-item"><span class="news-thumb" role="img" aria-label="Miniatura da notícia sobre silos"></span><span class="news-text">Monitoramento de silos reduz perdas na safra</span></li>
        <li class="news-item"><span class="news-thumb" role="img" aria-label="Miniatura da notícia sobre expurgo"></span><span class="news-text">Novas técnicas de expurgo em grãos</span></li>
        <li class="news-item"><span class="news-thumb" role="img" aria-label="Miniatura da notícia sobre roedores"></span><span class="news-text">Controle de roedores em armazéns rurais</span></li>
        <li class="news-item"><span class="news-thumb" role="img" aria-label="Miniatura da notícia sobre escorpiões"></span><span class="news-text">Cuidados com escorpiões no período chuvoso</span></li>
        <li class="news-item"><span class="news-thumb" role="img" aria-label="Miniatura da notícia sobre pragas urbanas"></span><span class="news-text">Manejo integrado de pragas urbanas</span></li>
      </ul>
    </aside>
  </main>
</body>
</html>
```